Security Services Business Card

Looking for a clean modern style business card design for a residential and commercial security solutions provider. We install and service the following
security alarm, access control, video surveillance and fire alarm. Attached are the front and back of our current business cards in PSD file format.

Target Market(s)

Security alarm clients in the commercial and residential markets

Industry/Entity Type

Security Service

Contact Information for Business Card

We are open to designers suggestion and or design ideas.

Font styles to use
Serif
Sans Serif

Colors
3276b5
33a6d7
fffefd

Requirements
Must have
• Must have company logo , first and last name , phone number , web and email address, ect....

```html
<!DOCTYPE html>
<html lang="en">
<head>
<meta charset="utf-8">
<title>Vantorel Systems – Business Card</title>
<link href="https://fonts.googleapis.com/css2?family=Montserrat:wght@400;700&display=swap" rel="stylesheet">
<style>
  :root{
    --backdrop:#959595;
    --paper:#fffefd;
    --brand-blue:#3276b5;
    --sky-blue:#33a6d7;
    --card-navy:#2f49a8;
    --logo-deep:#24399a;
    --ink-grey:#5b5b5b;
  }
  *{margin:0;padding:0;box-sizing:border-box}
  html,body{width:1200px;height:801px;overflow:hidden}
  body{
    background:var(--backdrop);
    font-family:"Montserrat",Arial,sans-serif;
    display:flex;align-items:center;justify-content:center;gap:40px;
  }
  .card{
    width:540px;height:309px;position:relative;overflow:hidden;
    box-shadow:0 10px 24px rgba(0,0,0,.25);
  }
  /* Front */
  .card-front{background:var(--paper);color:var(--ink-grey)}
  .front-brand{
    position:absolute;left:30px;top:102px;width:250px;
    display:flex;align-items:center;gap:8px;white-space:nowrap;
    color:var(--sky-blue);font-weight:700;font-size:21px;letter-spacing:.3px;
  }
  .brand-dot{width:12px;height:12px;border-radius:50%;background:var(--sky-blue);flex:none}
  .address{
    position:absolute;left:50px;top:180px;
    font-size:13.5px;line-height:1.45;
  }
  .person{position:absolute;left:300px;top:70px}
  .person-name{color:var(--sky-blue);font-weight:700;font-size:21px;line-height:1.1}
  .person-title{font-size:15px;margin-top:4px}
  .contacts{position:absolute;left:300px;top:148px;list-style:none;font-size:13px;line-height:1.6}
  .contacts li{display:flex;align-items:center;gap:8px;white-space:nowrap}
  .contacts svg{width:11px;height:11px;fill:var(--sky-blue);flex:none}
  /* Back */
  .card-back{background:linear-gradient(160deg,#3450b0,var(--card-navy) 60%,#2a43a0)}
  .back-brand{
    position:absolute;left:0;right:0;top:98px;text-align:center;white-space:nowrap;
    color:var(--logo-deep);font-weight:700;font-size:44px;letter-spacing:1px;
  }
  .services{
    position:absolute;left:0;right:0;bottom:44px;text-align:center;white-space:nowrap;
    color:var(--sky-blue);font-weight:700;font-size:14px;letter-spacing:.3px;
  }
</style>
</head>
<body>
  <section class="card card-front">
    <div class="front-brand"><span class="brand-dot"></span>Vantorel Systems</div>
    <p class="address">4120 Marlow Ave # 310,<br>Brookfield Ohio 44403</p>
    <div class="person">
      <h1 class="person-name">Daniel Pryce</h1>
      <p class="person-title">Director</p>
    </div>
    <ul class="contacts">
      <li><svg viewBox="0 0 24 24" aria-hidden="true"><path d="M6.6 10.8a15 15 0 0 0 6.6 6.6l2.2-2.2c.3-.3.7-.4 1-.2 1.1.4 2.3.6 3.6.6.6 0 1 .4 1 1V20c0 .6-.4 1-1 1A17 17 0 0 1 3 4c0-.6.4-1 1-1h3.5c.6 0 1 .4 1 1 0 1.3.2 2.5.6 3.6.1.3 0 .7-.2 1z"/></svg>555.014.2277 ext 106</li>
      <li><svg viewBox="0 0 24 24" aria-hidden="true"><path d="M2 5h20v14H2zM3.5 6.5 12 13l8.5-6.5z"/></svg>name@vantorelsecure.com</li>
      <li><svg viewBox="0 0 24 24" aria-hidden="true"><circle cx="12" cy="12" r="10"/></svg>www.vantorelsecure.com</li>
    </ul>
  </section>

  <section class="card card-back">
    <div class="back-brand">Vantorel Systems</div>
    <p class="services">Video Surveillance • Security Alarm • Fire Alarm • Access Control</p>
  </section>
</body>
</html>
```